Brisko Sky Park needs a new upscale business card design for our high end aircraft hangar complex

Brisko Sky Park (BSP) is a large, upscale jet hangar complex in the US housing expensive aircraft. We need a new business card design, using our current logo. We will be attending a industry convention and need a card design that will stand out and be remembered by aircraft owners and private pilots.

Target Market(s)

Aircraft pilots or owners looking for a new upscale hangar

Industry/Entity Type

Airport

Contact Information for Business Card

I like to use very heavy card stock, 400#, double sided. Square, no rounded edges please.

Colors
3276b5
0255a3
85abd2

Requirements
Must have
• An expensive, classy design, vivid colors.
Nice to have
• Needs to look very expensive and classy, and have some "pop". Designer must be able to download or copy my current typeface or fonts.
• One card side might be black with the "Logo and Brisko Sky Park Double line image in blue (or try gold, or glossy black), and perhaps have a grayed out "K480 jet silhouette". The other card side would have our contact info, and perhaps the "BSP Logo only". I'd like my contact info 'stacked', not in a paragraph format.
Should not have
• Should not look "too busy". Having a double-sided card will help.

```html
<!DOCTYPE html>
<html lang="en">
<head>
<meta charset="utf-8">
<title>Brisko Sky Park – Business Card</title>
<link rel="stylesheet" href="https://fonts.googleapis.com/css2?family=Source+Sans+3:wght@400;600&display=swap">
<style>
  :root {
    --stage: #000000;
    --card-front: #2c76b2;
    --card-back-top: #1d8ac3;
    --card-back-bottom: #0f64a2;
    --ink: #ffffff;
    --ink-soft: #e6f0f8;
    --rule: #9cc6e6;
    --edge: #5aa0d2;
  }
  * { margin: 0; padding: 0; box-sizing: border-box; }
  html, body { width: 1200px; height: 900px; overflow: hidden; background: var(--stage); }
  body { position: relative; font-family: "Source Sans 3", "Myriad Pro", sans-serif; color: var(--ink); }

  .card {
    position: absolute;
    top: 275px;
    width: 476px;
    height: 292px;
    overflow: hidden;
    border-radius: 0;
    box-shadow: 0 0 0 1px var(--edge) inset, 0 2px 6px rgba(0,0,0,.6);
  }
  .card--front {
    left: 116px;
    background: var(--card-front);
  }
  .card--back {
    left: 622px;
    background: linear-gradient(180deg, var(--card-back-top), var(--card-back-bottom));
  }

  .brand-name {
    position: absolute;
    font-weight: 600;
    color: var(--ink);
    white-space: nowrap;
    letter-spacing: .3px;
    line-height: 1.2;
  }
  .card--front .brand-name { left: 224px; top: 104px; font-size: 27px; }
  .card--back .brand-name { left: 0; right: 0; top: 159px; text-align: center; font-size: 34px; }

  .person { position: absolute; left: 37px; top: 120px; }
  .person__name { font-size: 20px; font-weight: 400; line-height: 24px; }
  .person__role { font-size: 13px; line-height: 16px; color: var(--ink-soft); }

  .divider {
    position: absolute;
    left: 0; right: 0; top: 171px;
    height: 1px;
    background: var(--rule);
  }

  .contact-list {
    position: absolute;
    left: 221px; top: 189px;
    list-style: none;
  }
  .contact-list li {
    display: flex;
    align-items: center;
    gap: 8px;
    font-size: 13px;
    line-height: 19.7px;
  }
  .contact-list svg { width: 10px; height: 10px; fill: var(--ink); flex: none; }

  .address {
    position: absolute;
    left: 0; right: 0; top: 213px;
    text-align: center;
    font-size: 13px;
  }
</style>
</head>
<body>

<section class="card card--front">
  <div class="brand-name">Brisko Sky Park</div>

  <div class="person">
    <p class="person__name">Daniel Harper</p>
    <p class="person__role">Managing Director</p>
  </div>

  <div class="divider"></div>

  <ul class="contact-list">
    <li>
      <svg viewBox="0 0 10 10" aria-hidden="true"><path d="M2 0.5 L3.6 2.8 L2.8 3.8 Q4 6 6.2 7.2 L7.2 6.4 L9.5 8 L8.4 9.5 Q3.5 9 0.5 1.6 Z"/></svg>
      (055)-310-2284
    </li>
    <li>
      <svg viewBox="0 0 10 10" aria-hidden="true"><path d="M2 0.5 H7 V3 H9.5 V9.5 H0.5 V3 H2 Z M3 1.5 V3 H6 V1.5 Z M2 5 V6 H3 V5 Z M4.5 5 V6 H5.5 V5 Z M7 5 V6 H8 V5 Z M2 7 V8 H3 V7 Z M4.5 7 V8 H5.5 V7 Z M7 7 V8 H8 V7 Z" fill-rule="evenodd"/></svg>
      555-310-2290
    </li>
    <li>
      <svg viewBox="0 0 10 10" aria-hidden="true"><path d="M0.5 2 H9.5 V8.5 H0.5 Z M1.3 2.6 L5 5.6 L8.7 2.6" fill="none" stroke="#fff" stroke-width="1"/><path d="M0.5 2 H9.5 L5 5.6 Z"/></svg>
      info@briskosky.com
    </li>
    <li>
      <svg viewBox="0 0 10 10" aria-hidden="true"><circle cx="5" cy="5" r="4.5"/><path d="M3 2.5 Q4.5 3 4 4.5 Q2.5 5 3.5 7 M6.5 6 Q7.5 6.5 7 8" fill="none" stroke="#2c76b2" stroke-width=".9"/></svg>
      www.briskosky.com
    </li>
  </ul>
</section>

<section class="card card--back">
  <div class="brand-name">Brisko Sky Park</div>
  <p class="address">4820, Hangar Row Lane Milford, United States, 52190.</p>
</section>

</body>
</html>
```